Pell Clinic Standing Banner

Design a standing banner for a community health care clinic. Our website is www.pellclinic.org. On there you can find our list of services. I have uploaded our logo, mission/vision/about us statements, as well as our business cards for contact information and so you have an idea of the theme we are going for.
Our tagline is building a healthier society.

We want the banner to showcase our name, tagline, services, and the contact methods listed on the business card except for the address.

```html
<!DOCTYPE html>
<html lang="en">
<head>
<meta charset="utf-8">
<title>Pell Clinic Standing Banner</title>
<link rel="stylesheet" href="https://fonts.googleapis.com/css2?family=Bebas+Neue&family=Montserrat:wght@700&family=Oswald:wght@500;600&display=swap">
<style>
  :root {
    --stage: #4d4d4d;
    --green: #58b947;
    --green-dark: #3f9a33;
    --ink: #262626;
    --white: #ffffff;
    --footer: #2b2b2b;
    --line: #6b6b6b;
    --mark: #f2f2f2;
  }
  * { margin: 0; padding: 0; box-sizing: border-box; }
  html, body { width: 1200px; height: 2387px; overflow: hidden; }
  body { background: var(--stage); position: relative; }

  .banner {
    position: absolute; left: 87px; top: 0;
    width: 1025px; height: 2387px;
    background: var(--white);
    overflow: hidden;
  }

  .header {
    position: absolute; left: 0; top: 0; width: 1025px; height: 548px;
    background: var(--green);
  }
  .brand-mark {
    position: absolute; left: 432px; top: 48px;
    width: 160px; height: 160px; border-radius: 50%;
    background: var(--mark);
  }
  .brand-name {
    position: absolute; left: 0; right: 0; top: 240px;
    text-align: center;
    font-family: "Montserrat", sans-serif; font-weight: 700;
    font-size: 140px; line-height: 1; letter-spacing: -1px;
    color: var(--white);
  }

  .hero { position: absolute; left: 0; top: 548px; width: 1025px; height: 565px; }
  .hero-photo {
    position: absolute; inset: 0;
    background:
      radial-gradient(circle at 52% 58%, rgba(255,248,225,0.95) 0%, rgba(247,214,150,0.85) 12%, rgba(214,178,140,0.55) 28%, rgba(180,160,150,0) 48%),
      radial-gradient(ellipse at 60% 20%, rgba(196,160,130,0.55) 0%, rgba(196,160,130,0) 45%),
      linear-gradient(100deg, #b9cbe2 0%, #a9b8cc 35%, #b8a8a0 65%, #cfdcec 100%);
  }
  .hero-curve { position: absolute; inset: 0; }

  .tagline {
    position: absolute; left: 0; right: 0; top: 1170px;
    text-align: center;
    font-family: "Bebas Neue", sans-serif;
    font-size: 138px; line-height: 0.87; letter-spacing: -1px;
  }
  .tagline-lead { display: block; color: var(--green); }
  .tagline-main { display: block; color: var(--ink); }

  .services-tree { position: absolute; left: 0; top: 1440px; width: 1025px; height: 700px; }
  .services-pill {
    position: absolute; left: 362px; top: 1447px; width: 302px; height: 57px;
    border-radius: 29px; background: var(--green);
    color: var(--white); text-align: center;
    font-family: "Bebas Neue", sans-serif; font-size: 50px; line-height: 60px; letter-spacing: 1px;
  }

  .service-card {
    position: absolute; width: 294px; height: 268px;
    background: var(--white);
    border: 6px solid #ececec; border-radius: 12px;
    box-shadow: 0 2px 4px rgba(0,0,0,0.12);
    overflow: hidden;
  }
  .service-photo { position: absolute; left: 0; top: 0; width: 100%; height: 194px; }
  .service-label {
    position: absolute; left: 0; bottom: 0; width: 100%; height: 62px;
    background: linear-gradient(var(--green), var(--green-dark));
    color: var(--white); text-align: center;
    font-family: "Oswald", sans-serif; font-weight: 500;
    font-size: 29px; line-height: 62px; letter-spacing: 0;
    text-transform: uppercase;
  }
  .col-1 { left: 49px; } .col-2 { left: 365px; } .col-3 { left: 683px; }
  .row-1 { top: 1538px; } .row-2 { top: 1826px; }

  .photo-fairs { background: radial-gradient(ellipse at 40% 75%, #e8c4ab 0%, rgba(232,196,171,0) 45%), linear-gradient(135deg, #f1f4f8 0%, #d4deea 50%, #93a6c2 100%); }
  .photo-clinic { background: radial-gradient(ellipse at 80% 45%, #e3cfae 0%, rgba(227,207,174,0) 35%), linear-gradient(180deg, #f4f5f7 0%, #dfe3e8 55%, #8e949c 80%, #b9bec6 100%); }
  .photo-substance { background: radial-gradient(ellipse at 25% 45%, #ffffff 0%, rgba(255,255,255,0) 30%), linear-gradient(180deg, #f0f2f6 0%, #d3d9e2 60%, #9ea7b6 100%); }
  .photo-lab { background: radial-gradient(ellipse at 45% 55%, #e9c3a9 0%, rgba(233,195,169,0) 50%), radial-gradient(ellipse at 25% 75%, #9fd3ee 0%, rgba(159,211,238,0) 40%), linear-gradient(135deg, #8fcfb6 0%, #c9dcd2 100%); }
  .photo-research { background: radial-gradient(ellipse at 72% 80%, #c26a8c 0%, rgba(194,106,140,0) 35%), radial-gradient(ellipse at 30% 70%, #f5f0e6 0%, rgba(245,240,230,0) 40%), linear-gradient(135deg, #e8edf3 0%, #cfd7e2 100%); }
  .photo-nutrition { background: radial-gradient(ellipse at 70% 80%, #76b94a 0%, rgba(118,185,74,0) 45%), radial-gradient(ellipse at 75% 45%, #e0583a 0%, rgba(224,88,58,0) 35%), linear-gradient(135deg, #f4e8e4 0%, #e9c1b2 55%, #d98c6b 100%); }

  .call-band {
    position: absolute; left: 0; top: 2134px; width: 1025px; height: 136px;
    background: var(--green);
    color: var(--white); text-align: center;
    font-family: "Bebas Neue", sans-serif; font-size: 132px; line-height: 146px;
  }
  .contact-bar {
    position: absolute; left: 0; top: 2270px; width: 1025px; height: 117px;
    background: var(--footer);
    display: flex; align-items: center; justify-content: center; gap: 26px;
    color: var(--white);
    font-family: "Oswald", sans-serif; font-weight: 600; font-size: 37px;
  }
  .contact-item { display: flex; align-items: center; gap: 18px; }
  .contact-icon { width: 40px; height: 40px; }
</style>
</head>
<body>
<main class="banner">
  <header class="header">
    <span class="brand-mark" aria-hidden="true"></span>
    <h1 class="brand-name">Pell Clinic</h1>
  </header>

  <section class="hero">
    <div class="hero-photo" role="img" aria-label="Photo of a hand with a stethoscope surrounded by glowing medical icons and a heartbeat line"></div>
    <svg class="hero-curve" width="1025" height="565" viewBox="0 0 1025 565">
      <path d="M0 427 Q512 703 1025 427 L1025 565 L0 565 Z" fill="#ffffff"/>
      <path d="M0 410 Q512 712 1025 410 L1025 427 Q512 697 0 427 Z" fill="#58b947"/>
    </svg>
  </section>

  <h2 class="tagline">
    <span class="tagline-lead">Building a</span>
    <span class="tagline-main">Healthier Society</span>
  </h2>

  <svg class="services-tree" width="1025" height="700" viewBox="0 1440 1025 700" fill="none" stroke="#6b6b6b" stroke-width="3">
    <path d="M173 1538 V1490 Q173 1476 187 1476 H837 Q851 1476 851 1490 V1538"/>
    <path d="M512 1504 V1538"/>
    <path d="M196 1806 V1826 M512 1806 V1826 M830 1806 V1826"/>
    <path d="M343 1960 H365 M659 1960 H683"/>
  </svg>
  <div class="services-pill">Our Services</div>

  <article class="service-card col-1 row-1">
    <div class="service-photo photo-fairs" role="img" aria-label="Photo of a blood pressure check at a health fair"></div>
    <div class="service-label">Health Fairs</div>
  </article>
  <article class="service-card col-2 row-1">
    <div class="service-photo photo-clinic" role="img" aria-label="Photo of clinic supplies in glass jars on a counter"></div>
    <div class="service-label">Community Clinic</div>
  </article>
  <article class="service-card col-3 row-1">
    <div class="service-photo photo-substance" role="img" aria-label="Photo of a medicine vial and syringe"></div>
    <div class="service-label">Substance Abuse</div>
  </article>
  <article class="service-card col-1 row-2">
    <div class="service-photo photo-lab" role="img" aria-label="Photo of a gloved hand drawing blood from an arm"></div>
    <div class="service-label">Lab</div>
  </article>
  <article class="service-card col-2 row-2">
    <div class="service-photo photo-research" role="img" aria-label="Photo of a researcher writing notes beside sample tubes"></div>
    <div class="service-label">Clinical Research</div>
  </article>
  <article class="service-card col-3 row-2">
    <div class="service-photo photo-nutrition" role="img" aria-label="Photo of fresh vegetables being prepared"></div>
    <div class="service-label">Nutrition</div>
  </article>

  <div class="call-band">Call Us : 555-214-0387</div>

  <footer class="contact-bar">
    <span class="contact-item">
      <svg class="contact-icon" viewBox="0 0 40 40"><circle cx="20" cy="20" r="19" fill="#58b947"/><rect x="10" y="13" width="20" height="14" rx="2" fill="#2b2b2b"/><path d="M10 14 L20 22 L30 14" fill="none" stroke="#58b947" stroke-width="2"/></svg>
      INFO@PELLCLINIC.ORG
    </span>
    <span class="contact-item">
      <svg class="contact-icon" viewBox="0 0 40 40"><circle cx="20" cy="20" r="19" fill="#58b947"/><g fill="none" stroke="#2b2b2b" stroke-width="2"><circle cx="20" cy="20" r="11"/><ellipse cx="20" cy="20" rx="5" ry="11"/><path d="M9 20 H31 M11 14 H29 M11 26 H29"/></g></svg>
      WWW.PELLCLINIC.ORG
    </span>
  </footer>
</main>
</body>
</html>
```